Need posters that inspire entrepreneurs

I want to create beautiful, inspiring wall art. I'm looking for a designer to create an awesome sample (note this sample is not for real use). The winning design will form the foundation of our art "style" so there will be LOTS of ongoing work for the winning designer.

It's your challenge to create a style that is clean, inspiring and timeless, and possibly can be adapted to different colour palettes.

Looking for a perfect execution of words, image and design.

The attached example shows one idea. It should serve as an idea only.

Format of the images should be either rectangular or square. Exact size is preferably UK A4 (US letter) or max A3. Assume that a display would consist of a 4 x 4 image grid so size needs to allow for that in a small to medium size office.

The quotes I want in the 3 samples (each in an individual poster - not combined in 1 poster). Each quote should have it's own, the reason for three is to prove the design work on more than one quote. The quotes are:

1) Failure is the condiment that gives success its flavor.
– Dorian Welsby

2) Whether you think you can or think you can’t, you’re right.
– Oswald Pike

3) Ever tried. Ever failed. No matter. Try Again. Fail again. Fail better.
– Lionel Marwick

Each design should include the image of the person and the quote + any design elements you consider relevant. You should find relevant images of the individuals being quoted. The final images will not be published or used commercially in any way.

Font styles to use
Serif
Sans Serif

Colors

Designer to choose colors to be used in the design.

Requirements
Must have
• Words and headshot image - 1 per poster design.
• Please consider in the design that there will not always be photographs of the person quoted and as such the design will need to hold, whether the source is a photo, sketch or something else.
Nice to have
• None, but note that the final image will be printed on a wall mounted board, printed to the edge but not on the edge. The board will have black or white edges so consider in the design.
Should not have
• None

```html
<!DOCTYPE html>
<html lang="en">
<head>
<meta charset="utf-8">
<title>Inspiring Quote Posters</title>
<link rel="stylesheet" href="https://fonts.googleapis.com/css2?family=Open+Sans:wght@300;400;700&display=swap">
<style>
  :root {
    --backdrop-top: #ffffff;
    --backdrop-mid: #dcdcdc;
    --scene-dark: #141414;
    --scene-mid: #262626;
    --scene-light: #363636;
    --figure-light: #5a5a5a;
    --figure-mid: #3e3e3e;
    --ink: #ffffff;
    --label-bg: #1a1a1a;
    --quote-mark: rgba(255, 255, 255, 0.18);
  }
  * { margin: 0; padding: 0; box-sizing: border-box; }
  html, body { width: 1200px; height: 1000px; overflow: hidden; }
  body {
    position: relative;
    font-family: "Open Sans", Arial, sans-serif;
    background: linear-gradient(180deg, var(--backdrop-top) 0%, var(--backdrop-mid) 38%, var(--backdrop-mid) 62%, var(--backdrop-top) 100%);
  }
  .poster {
    position: absolute;
    top: 286px;
    width: 389px;
    height: 388px;
    overflow: hidden;
    box-shadow: 2px 2px 4px rgba(0, 0, 0, 0.35);
  }
  .poster--welsby { left: 8px; }
  .poster--pike { left: 407px; }
  .poster--marwick { left: 805px; }

  .scene {
    position: absolute;
    inset: 0;
  }
  .poster--welsby .scene {
    background: linear-gradient(90deg, var(--scene-mid) 0%, var(--scene-light) 45%, var(--scene-mid) 100%);
  }
  .poster--pike .scene {
    background: linear-gradient(90deg, var(--scene-dark) 0%, var(--scene-mid) 50%, var(--scene-dark) 100%);
  }
  .poster--marwick .scene {
    background: linear-gradient(180deg, var(--scene-mid) 0%, var(--scene-light) 60%, var(--scene-mid) 100%);
  }

  .portrait {
    position: absolute;
    background: radial-gradient(ellipse at 50% 35%, var(--figure-light) 0%, var(--figure-mid) 45%, rgba(40, 40, 40, 0) 75%);
  }
  .poster--welsby .portrait { left: 60px; top: 0; width: 290px; height: 388px; }
  .poster--pike .portrait { left: 200px; top: 0; width: 200px; height: 388px; }
  .poster--marwick .portrait { left: 90px; top: 20px; width: 200px; height: 368px; }

  .quote-frame {
    position: absolute;
    border: 4px solid var(--ink);
  }
  .poster--welsby .quote-frame { left: 71px; top: 107px; width: 252px; height: 206px; }
  .poster--pike .quote-frame { left: 70px; top: 107px; width: 251px; height: 206px; }
  .poster--marwick .quote-frame { left: 70px; top: 104px; width: 252px; height: 206px; }

  .quote-mark {
    position: absolute;
    font-family: Georgia, "Times New Roman", serif;
    font-weight: 700;
    font-size: 64px;
    line-height: 1;
    color: var(--quote-mark);
  }
  .quote-mark--open { left: -24px; top: -26px; }
  .quote-mark--close { right: -26px; bottom: -54px; }

  .quote-text {
    position: absolute;
    left: -10px;
    right: -10px;
    color: var(--ink);
    text-align: center;
    font-weight: 300;
    font-size: 22.5px;
    line-height: 25.5px;
    text-transform: uppercase;
  }
  .quote-text strong { font-weight: 700; }
  .poster--welsby .quote-text { top: 37px; }
  .poster--pike .quote-text { top: 48px; }
  .poster--marwick .quote-text { top: 23px; }

  .author {
    position: absolute;
    bottom: -9px;
    left: 50%;
    transform: translateX(-50%);
    padding: 0 4px;
    background: var(--label-bg);
    color: var(--ink);
    font-weight: 400;
    font-size: 8px;
    line-height: 14px;
    letter-spacing: 0.2px;
    white-space: nowrap;
    text-transform: uppercase;
  }
</style>
</head>
<body>
  <section class="poster poster--welsby">
    <div class="scene"></div>
    <div class="portrait" role="img" aria-label="Headshot area: black and white portrait of Dorian Welsby in glasses and a suit before a building"></div>
    <div class="quote-frame">
      <span class="quote-mark quote-mark--open">&#8220;</span>
      <span class="quote-mark quote-mark--close">&#8221;</span>
      <p class="quote-text"><strong>Failure</strong><br>is the condiment<br>that gives<br><strong>success</strong><br>its flavor.</p>
      <span class="author">Dorian Welsby</span>
    </div>
  </section>

  <section class="poster poster--pike">
    <div class="scene"></div>
    <div class="portrait" role="img" aria-label="Headshot area: black and white photograph of Oswald Pike in a bowler hat and overcoat beside a vintage car"></div>
    <div class="quote-frame">
      <span class="quote-mark quote-mark--open">&#8220;</span>
      <span class="quote-mark quote-mark--close">&#8221;</span>
      <p class="quote-text">Whether you<br>think you <strong>can</strong> or<br>think you <strong>can’t,<br>you’re right</strong>.</p>
      <span class="author">Oswald Pike</span>
    </div>
  </section>

  <section class="poster poster--marwick">
    <div class="scene"></div>
    <div class="portrait" role="img" aria-label="Headshot area: black and white street photograph of Lionel Marwick walking away along a pavement"></div>
    <div class="quote-frame">
      <span class="quote-mark quote-mark--open">&#8220;</span>
      <span class="quote-mark quote-mark--close">&#8221;</span>
      <p class="quote-text">Ever tried.<br>Ever failed.<br>No matter.<br><strong>Try again.</strong><br>Fail again.<br>Fail better.</p>
      <span class="author">Lionel Marwick</span>
    </div>
  </section>
</body>
</html>
```